SEO Friendly Web Design Needed for Leading Software Company

Founded in 1986, TRVB is the market leader for innovative software solutions for the heavy civil construction industry. Our suite of products, including the bestsellers GroundQuote® and FieldTask®, are used by more than 40,000 workers every day to improve their proficiency at estimating, job management, resource management, safety and equipment maintenance. TRVB also offers new mobile applications and cloud computing services so companies can work on a wide array of devices including laptops, tablets and smartphones.

In addition to high quality software, TRVB is best known for providing world-class customer service, and for its friendly, employee-ownership culture. We offer a full range of professional support options to help customers maximize their software investment including implementation planning, training and INSTANT 24/7 phone support.

Goals, objectives and target audience

The goal of our new layout and design will be to increase conversions, enhance user experience and enhance our SERP rankings.

Our objectives are as follows:
1. Clean and well laid out home page. White space is OK.
2. CTAs in strategic locations throughout to drive conversions and MQLs
3. SEO rich content with appropriate layout to meet our SEO requirements
4. 2 Master Design Templates – Home & Internal
5. Custom Design elements for individual modules

Target Audience:
- Heavy / Civil Construction Industry
- C Level executives or persons in leadership roles who utilize our software
- MEN in the construction industry.

Requirements
Should not have
• Feminine design - our industry is largely male construction workers.
Don't use script or goofy fonts
Don't change the logo, or put it in an image where it is not easily viewable.

```html
<!DOCTYPE html>
<html lang="en">
<head>
<meta charset="utf-8">
<title>TRVB – Work Smarter</title>
<link href="https://fonts.googleapis.com/css2?family=Roboto:wght@300;400;700&display=swap" rel="stylesheet">
<style>
  :root {
    --green: #006838;
    --orange: #f7821e;
    --link-orange: #f08a24;
    --ink: #333333;
    --ink-soft: #4a4a4a;
    --band: #2b2b2b;
    --band-text: #cfcfcf;
    --footer-bg: #e8e8e8;
    --rule: #9a9a9a;
    --social: #9b9b9b;
    --white: #ffffff;
  }
  * { margin: 0; padding: 0; box-sizing: border-box; }
  html, body { width: 1200px; height: 684px; overflow: hidden; background: var(--white); }
  body { font-family: "Roboto", Arial, sans-serif; color: var(--ink); }
  .page { position: relative; width: 1200px; height: 684px; }

  /* Resource section */
  .resources { position: absolute; left: 0; top: 0; width: 1200px; height: 266px; background: var(--white); }
  .resources__title { position: absolute; left: 147px; top: 30px; font-size: 35px; font-weight: 300; color: var(--ink); letter-spacing: -0.3px; }
  .topic { position: absolute; top: 87px; }
  .topic--problems { left: 161px; }
  .topic--solutions { left: 444px; }
  .topic--cases { left: 728px; }
  .topic__icon { position: absolute; left: 0; top: 0; width: 79px; height: 79px; background: var(--white); border: 1px solid #d6d6d6; box-shadow: 0 1px 3px rgba(0,0,0,.25); padding: 4px; }
  .topic__icon svg { display: block; width: 69px; height: 69px; }
  .topic__name { position: absolute; left: 105px; top: 18px; width: 200px; font-size: 24px; font-weight: 300; line-height: 26px; color: var(--ink-soft); }
  .topic__links { position: absolute; left: 105px; top: 97px; list-style: none; width: 200px; }
  .topic__links li { font-size: 12px; line-height: 19px; color: var(--link-orange); }

  /* Call to action band */
  .cta-band { position: absolute; left: 0; top: 266px; width: 1200px; height: 75px; background: var(--band); }
  .cta-band__text { position: absolute; left: 147px; top: 26px; font-size: 19px; font-weight: 300; color: var(--band-text); }
  .cta-band__button { position: absolute; left: 784px; top: 10px; width: 82px; height: 42px; background: var(--orange); color: var(--white); font-size: 14px; font-weight: 700; line-height: 42px; text-align: center; }

  /* Footer */
  .site-footer { position: absolute; left: 0; top: 341px; width: 1200px; height: 320px; background: var(--footer-bg); }
  .footer-col { position: absolute; top: 60px; }
  .footer-col--software { left: 161px; }
  .footer-col--services { left: 285px; }
  .footer-col--news { left: 411px; }
  .footer-col--about { left: 535px; }
  .footer-col--contact { left: 661px; width: 150px; }
  .footer-col--social { left: 848px; }
  .footer-col__title { font-size: 21px; font-weight: 400; color: var(--ink); margin-bottom: 14px; }
  .footer-links { list-style: none; width: 98px; }
  .footer-links li { font-size: 11px; line-height: 15px; padding-top: 1px; color: var(--link-orange); border-bottom: 1px solid var(--rule); margin-bottom: 1px; }
  .contact-line { font-size: 11px; line-height: 14px; color: var(--ink); margin-bottom: 17px; }
  .contact-line b { font-weight: 700; }
  .social-list { list-style: none; }
  .social-list li { display: flex; align-items: center; height: 35px; font-size: 10px; color: var(--social); }
  .social-list__mark { width: 21px; height: 21px; background: var(--social); margin-right: 7px; }

  .footer-strip { position: absolute; left: 0; top: 661px; width: 1200px; height: 23px; background: var(--band); }
</style>
</head>
<body>
<div class="page">

  <section class="resources">
    <h1 class="resources__title">Work Smarter - Content Resource Section</h1>

    <div class="topic topic--problems">
      <div class="topic__icon">
        <svg viewBox="0 0 69 69" aria-hidden="true">
          <rect width="69" height="69" fill="var(--green)"/>
          <circle cx="34.5" cy="34.5" r="15" fill="#111"/>
          <path d="M28 28 L41 41 M41 28 L28 41" stroke="#fff" stroke-width="3.5" stroke-linecap="round"/>
        </svg>
      </div>
      <h2 class="topic__name">Construction<br>Problems</h2>
      <ul class="topic__links"><li>Link to Content Home</li><li>Link to Content Home</li><li>Link to Content Home</li></ul>
    </div>

    <div class="topic topic--solutions">
      <div class="topic__icon">
        <svg viewBox="0 0 69 69" aria-hidden="true">
          <rect width="69" height="69" fill="var(--green)"/>
          <circle cx="34.5" cy="30" r="10" fill="#111"/>
          <rect x="30" y="37" width="9" height="8" fill="#111"/>
          <rect x="31" y="46" width="7" height="3" fill="#111"/>
        </svg>
      </div>
      <h2 class="topic__name">Construction<br>Solutions</h2>
      <ul class="topic__links"><li>Link to Content Home</li><li>Link to Content Home</li><li>Link to Content Home</li></ul>
    </div>

    <div class="topic topic--cases">
      <div class="topic__icon">
        <svg viewBox="0 0 69 69" aria-hidden="true">
          <rect width="69" height="69" fill="var(--green)"/>
          <path d="M17 23 L27 19 L27 46 L17 50 Z M29 19 L40 23 L40 50 L29 46 Z M42 23 L52 19 L52 46 L42 50 Z" fill="#111"/>
        </svg>
      </div>
      <h2 class="topic__name">Case<br>Studies</h2>
      <ul class="topic__links"><li>Link to Content Home</li><li>Link to Content Home</li><li>Link to Content Home</li></ul>
    </div>
  </section>

  <section class="cta-band">
    <p class="cta-band__text">Simple text overview to generate action for CTA.</p>
    <div class="cta-band__button">CTA</div>
  </section>

  <footer class="site-footer">
    <div class="footer-col footer-col--software">
      <h3 class="footer-col__title">Software</h3>
      <ul class="footer-links">
        <li>GroundQuote</li><li>FieldTask</li><li>Safety Application</li><li>The Router</li><li>GPS</li><li>FleetCare 360</li><li>TankLog Plus</li><li>pastbids.net</li><li>Mobile Apps</li>
      </ul>
    </div>
    <div class="footer-col footer-col--services">
      <h3 class="footer-col__title">Services</h3>
      <ul class="footer-links">
        <li>Cloud Services</li><li>Custom Programming</li><li>Universities</li><li>Instant Support</li><li>Training &amp; Events</li><li>Training Options</li>
      </ul>
    </div>
    <div class="footer-col footer-col--news">
      <h3 class="footer-col__title">News</h3>
      <ul class="footer-links">
        <li>Newsroom</li><li>Newsletter</li><li>Press Kit</li><li>Newsletter subscription</li><li>Training &amp; Events</li><li>Careers at TRVB</li><li>Careers in Construction</li>
      </ul>
    </div>
    <div class="footer-col footer-col--about">
      <h3 class="footer-col__title">About Us</h3>
      <ul class="footer-links">
        <li>About TRVB</li><li>TRVB Culture Blog</li><li>Our Clients</li><li>Contact/More Info</li><li>The TRVB Story</li><li>Map &amp; Directions</li><li>Stability</li><li>Why Choose TRVB</li>
      </ul>
    </div>
    <div class="footer-col footer-col--contact">
      <h3 class="footer-col__title">TRVB</h3>
      <p class="contact-line"><b>Sales:</b> 800-555-0147</p>
      <p class="contact-line"><b>Support:</b> 800-555-0192</p>
      <p class="contact-line"><b>Email:</b> info@trvb.com</p>
      <p class="contact-line">4820 W. Meridian Blvd. Cedar Falls, Tx 77512</p>
    </div>
    <div class="footer-col footer-col--social">
      <h3 class="footer-col__title">Social</h3>
      <ul class="social-list">
        <li><span class="social-list__mark"></span>Chirper</li>
        <li><span class="social-list__mark"></span>Friendbook</li>
        <li><span class="social-list__mark"></span>Circlenet</li>
        <li><span class="social-list__mark"></span>Worklink</li>
      </ul>
    </div>
  </footer>

  <div class="footer-strip"></div>
</div>
</body>
</html>
```